Product flyer with pricing

We manufacture iconic and luxury vending trailers. for our first trailer we need a flyer created to give to prospective clients with base pricing. I am uploading an example along with graphic files.

```html
<!DOCTYPE html>
<html lang="en">
<head>
<meta charset="utf-8">
<title>Meadow Cottage Mini – Vending Trailer Flyer</title>
<link rel="stylesheet" href="https://fonts.googleapis.com/css2?family=Fira+Sans+Condensed:wght@600;700&family=Source+Sans+3:wght@400;600;700&family=Lobster&display=swap">
<style>
  :root{
    --green:#3d9b35;
    --green-dark:#2b8a2e;
    --orange:#f0a623;
    --text:#4a4a4a;
    --muted:#6b6b6b;
    --white:#ffffff;
    --stage:#e9e9e7;
    --photo-sky:#6c9ed6;
    --photo-ground:#7d8186;
  }
  *{box-sizing:border-box;margin:0;padding:0}
  html,body{width:1200px;height:827px;overflow:hidden;background:var(--stage)}
  body{font-family:"Source Sans 3",sans-serif;color:var(--text)}
  .flyer{position:absolute;left:294px;top:17px;width:612px;height:792px;background:var(--white);box-shadow:0 2px 10px rgba(0,0,0,.18);overflow:hidden}
  .brand{position:absolute;left:16px;top:64px;display:flex;align-items:center;gap:7px;font-family:"Fira Sans Condensed",sans-serif;font-weight:700;font-size:19px;color:var(--orange);text-transform:uppercase}
  .brand-dot{width:14px;height:14px;border-radius:50%;background:var(--green)}
  .title{position:absolute;right:14px;top:20px;text-align:right}
  .title h1{font-family:"Fira Sans Condensed",sans-serif;font-weight:600;font-size:23px;color:var(--green-dark);line-height:1}
  .title p{margin-top:6px;font-size:12.5px;letter-spacing:3.3px;color:var(--muted);font-weight:600}
  .hero{position:absolute;left:0;top:76px;width:612px;height:252px}
  .use-cases{position:absolute;left:0;top:329px;width:612px;height:104px;background:var(--orange)}
  .use-tab{position:absolute;left:25px;top:8px;width:20px;height:90px;background:var(--green);border-radius:0 6px 6px 0;display:flex;align-items:center;justify-content:center}
  .use-tab span{transform:rotate(-90deg);white-space:nowrap;color:var(--white);font-weight:700;font-size:12px;letter-spacing:.5px}
  .use-list{position:absolute;left:60px;top:12px;list-style:none}
  .use-list li{display:flex;align-items:center;gap:6px;height:23px;font-size:11.5px;color:var(--white)}
  .use-list svg{width:14px;height:14px;flex:none}
  .use-list b{color:#eaf37a;font-weight:600}
  .price{position:absolute;left:477px;top:306px;width:122px;height:122px;border-radius:50%;background:var(--green);border:3px dotted #7fc46a;display:flex;flex-direction:column;align-items:center;justify-content:center;color:var(--white);box-shadow:0 0 0 3px var(--green)}
  .price small{font-weight:700;font-size:11px}
  .price strong{font-weight:700;font-size:23px;line-height:1.1}
  .price sup{font-size:11px}
  .specs{position:absolute;top:446px;width:290px}
  .specs.features{left:25px}
  .specs.options{left:310px}
  .specs h2{font-size:13.5px;font-weight:700;color:var(--green)}
  .specs ul{list-style:none;margin-top:6px}
  .specs li{position:relative;padding-left:12px;font-size:8.3px;line-height:1.22;margin-bottom:3.4px}
  .specs li::before{content:"";position:absolute;left:0;top:2px;width:6px;height:6px;border-radius:50%;background:var(--green)}
  .specs li b{font-weight:700}
  .gallery{position:absolute;left:26px;top:583px;display:flex;gap:27px}
  .thumb{width:166px;height:112px;background:var(--white);padding:4px;box-shadow:0 1px 4px rgba(0,0,0,.3)}
  .thumb div{width:100%;height:100%;background:linear-gradient(180deg,var(--photo-sky) 0%,#c9d4de 48%,#eef0f0 60%,var(--photo-ground) 100%)}
  .tagline{position:absolute;left:0;width:612px;top:706px;text-align:center;font-family:"Lobster",cursive;font-size:20px;color:var(--green)}
  .contact-tab{position:absolute;left:24px;top:729px;width:180px;height:28px;background:var(--orange);border-radius:10px 10px 0 0;color:var(--white);font-weight:700;font-size:15px;padding:4px 0 0 27px}
  .contact-bar{position:absolute;left:0;top:748px;width:612px;height:44px;background:var(--green);display:flex;align-items:center;color:var(--white);font-weight:600;font-size:13.5px}
  .contact-bar span{position:absolute;display:flex;align-items:center;gap:5px}
  .contact-bar svg{width:12px;height:12px}
</style>
</head>
<body>
<main class="flyer">
  <div class="brand"><span class="brand-dot"></span>Brightnest Cabins</div>

  <header class="title">
    <h1>The “Meadow Cottage Mini”</h1>
    <p>LUXURY, MOBILE VENDING HOUSE</p>
  </header>

  <svg class="hero" viewBox="0 0 612 252" aria-hidden="false">
    <path d="M0 110 C150 30 380 0 612 4 L612 14 C380 12 160 40 0 130 Z" fill="var(--orange)"/>
    <path role="img" aria-label="Photo of the white board-and-batten vending trailer towed by a pickup truck in a parking lot" d="M0 130 C160 40 380 12 612 14 L612 252 L0 252 Z" fill="url(#heroGrad)"/>
    <defs>
      <linearGradient id="heroGrad" x1="0" y1="0" x2="0" y2="1">
        <stop offset="0" stop-color="#4f86cf"/>
        <stop offset=".45" stop-color="#b9c9d8"/>
        <stop offset=".55" stop-color="#e6e8e8"/>
        <stop offset="1" stop-color="#6f7378"/>
      </linearGradient>
    </defs>
  </svg>

  <section class="use-cases">
    <div class="use-tab"><span>USE CASES</span></div>
    <ul class="use-list">
      <li><svg viewBox="0 0 14 14"><rect x="2" y="4" width="8" height="8" fill="#fff"/><rect x="10" y="6" width="3" height="3" fill="none" stroke="#fff" stroke-width="1.4"/></svg><span><b>FOOD:</b> Lemonade, Coffee, pizza, cookies, doughnuts, barbecue and more!</span></li>
      <li><svg viewBox="0 0 14 14"><path d="M1 7 L7 1 L13 7 H11 V13 H3 V7 Z" fill="#fff"/></svg><span><b>RETAIL:</b> Clothing, watches, jewelry, flowers and more!</span></li>
      <li><svg viewBox="0 0 14 14"><path d="M0 6 L4 4 L7 6 L10 4 L14 6 L10 10 L7 11 L4 10 Z" fill="#fff"/></svg><span><b>CORPORATE:</b> Product info, demonstration, information, brand awareness.</span></li>
      <li><svg viewBox="0 0 14 14"><circle cx="7" cy="5" r="4" fill="#fff"/><rect x="5" y="9" width="4" height="4" fill="#fff"/></svg><span><b>FUNDRAISERS:</b> Girls/boy sports, non profits, etc.</span></li>
    </ul>
  </section>

  <div class="price"><small>BASE PRICE:</small><strong><sup>$</sup>45,000</strong></div>

  <section class="specs features">
    <h2>BASE UNIT FEATURES:</h2>
    <ul>
      <li>Trailer features tandem wheels w/ brakes</li>
      <li>Steel frame construction for fire retardation safety &amp; weight reduction</li>
      <li>100% off grid with solar and lithium battery system allowing the trailer to be used in places not accessible by traditional trailers</li>
      <li>80 gallon water supply tank</li>
      <li>100 gallon waste water tank</li>
      <li>Cupboards, cabinets &amp; four stainless steel sinks</li>
      <li>60” Gas shock serving window</li>
    </ul>
  </section>

  <section class="specs options">
    <h2>AVAILABLE OPTIONS:</h2>
    <ul>
      <li>HVAC - Aerolux Mini Split - <b>$1,800</b></li>
      <li>Cooler / Glass front Commercial refrigerator - <b>$1,600</b></li>
      <li>Upper loft storage area - <b>$1,200</b></li>
      <li>Signage and graphics - <b>$2,000 - $5,000</b> depend on complexity</li>
      <li>Ice machine - <b>$1,100</b></li>
      <li>Other custom items available on request.</li>
    </ul>
  </section>

  <div class="gallery">
    <figure class="thumb"><div role="img" aria-label="Photo of the trailer from the front corner"></div></figure>
    <figure class="thumb"><div role="img" aria-label="Photo of the trailer from the front"></div></figure>
    <figure class="thumb"><div role="img" aria-label="Photo of the trailer side with serving window"></div></figure>
  </div>

  <p class="tagline">Luxury Vending Trailers</p>

  <div class="contact-tab">CONTACT US</div>
  <footer class="contact-bar">
    <span style="left:24px"><svg viewBox="0 0 12 12"><circle cx="6" cy="6" r="5.3" fill="none" stroke="#fff" stroke-width="1.2"/><rect x="3" y="4" width="6" height="4" fill="#fff"/></svg>hello@brightnestcabins.com</span>
    <span style="left:248px"><svg viewBox="0 0 12 12"><circle cx="6" cy="6" r="5.3" fill="none" stroke="#fff" stroke-width="1.2"/><path d="M4 3 L5 5 L4.5 6 Q5.5 7.5 7 8 L8 7.5 L9 9 Q7 10 5 8 Q3 6 4 3 Z" fill="#fff"/></svg>0100 555 012</span>
    <span style="left:378px"><svg viewBox="0 0 12 12"><circle cx="6" cy="6" r="5.3" fill="none" stroke="#fff" stroke-width="1.2"/><circle cx="6" cy="6" r="2.5" fill="none" stroke="#fff" stroke-width="1"/></svg>www.BrightnestCabins.com</span>
  </footer>
</main>
</body>
</html>
```